Nine Rung Ledger Remedy Seminar

I would like a flyer to hand out to participants at the speeches that we give. We are a CPA firm that specializes in entrepreneurs and realtors. We would like a flyer that looks crisp and clean, that integrates our logo and our company colors (shades of blue & gold). We would like the wording to be as laid out in the attached documents, but design is up to you. We would like a picture to go along with each point and are open to ideas. The flyer should be one page, preferably just the front.

Colors
3176b5
fee18a

Requirements
Must have
• Our logo and the wording supplied.
• A picture to go along with each topic.
Nice to have
• Images that pop, clean look, professional.
Should not have
• Look messy.

```html
<!DOCTYPE html>
<html lang="en">
<head>
<meta charset="utf-8">
<title>Nine Rung Ledger Remedy Seminar Agenda</title>
<link href="https://fonts.googleapis.com/css2?family=Anton&family=Lato:ital,wght@0,400;0,700;0,900;1,700&display=swap" rel="stylesheet">
<style>
  :root{
    --brand-blue:#3176b5;
    --title-blue:#1d5da6;
    --gold:#fee18a;
    --gold-deep:#f5cf5e;
    --ink:#1b1b1b;
    --rule:#3a3a3a;
    --white:#ffffff;
  }
  html,body{margin:0;padding:0;}
  body{width:869px;height:1200px;overflow:hidden;background:var(--white);font-family:"Lato",sans-serif;color:var(--ink);}
  .flyer{position:relative;width:869px;height:1200px;background:var(--white);}
  .masthead{position:absolute;left:0;top:0;width:869px;height:90px;background:linear-gradient(180deg,var(--gold-deep) 0%,var(--gold) 100%);display:flex;align-items:center;justify-content:center;}
  .masthead h1{margin:0;font-family:"Anton",sans-serif;font-weight:400;font-size:41px;letter-spacing:.3px;color:var(--title-blue);}

  .step{position:absolute;left:0;width:869px;}
  .step-text{position:absolute;left:51px;width:479px;top:0;bottom:0;border:1.5px solid var(--rule);box-sizing:border-box;padding:0 14px 0 56px;display:flex;align-items:center;}
  .step-text p{margin:0;font-size:15px;line-height:20.5px;text-align:justify;}
  .step-text b{font-weight:900;}
  .step-badge{position:absolute;left:22px;top:50%;width:60px;height:60px;margin-top:-30px;border-radius:50%;background:var(--brand-blue);color:var(--white);font-family:"Anton",sans-serif;font-size:19px;line-height:18px;text-align:center;display:flex;flex-direction:column;justify-content:center;}
  .step-photo{position:absolute;left:566px;width:288px;top:-4px;bottom:-4px;border:2px solid var(--brand-blue);box-sizing:border-box;}

  .photo-selfemploy{background:linear-gradient(135deg,#e6e94a 0%,#c9c23c 55%,#7d8a62 100%);}
  .photo-keys{background:linear-gradient(120deg,#d9a884 0%,#eaeaea 55%,#c9cfd8 100%);}
  .photo-notebook{background:linear-gradient(120deg,#8a7a5e 0%,#f1f1ee 40%,#e4e6ea 100%);}
  .photo-planning{background:linear-gradient(130deg,#5b7796 0%,#e9e6dc 50%,#b98d6a 100%);}
  .photo-taxcut{background:linear-gradient(120deg,#ffffff 0%,#f2c3c3 45%,#e45d63 60%,#ffffff 100%);}
  .photo-desk{background:linear-gradient(120deg,#a57b55 0%,#d7c6a7 40%,#4b5a6f 75%,#9a7553 100%);}
  .photo-card{background:linear-gradient(120deg,#c9c9c9 0%,#f3f3f3 40%,#8a8d93 100%);}

  .footer{position:absolute;left:0;top:1077px;width:869px;height:123px;background:var(--brand-blue);color:var(--white);}
  .footer .motto{position:absolute;left:26px;top:18px;margin:0;font-weight:900;font-size:15px;letter-spacing:.2px;}
  .contact{position:absolute;left:26px;top:57px;font-size:10.5px;line-height:21px;}
  .contact-row{display:flex;align-items:center;gap:14px;white-space:nowrap;}
  .contact-item{display:inline-flex;align-items:center;gap:5px;}
  .contact svg{width:12px;height:12px;fill:var(--gold);flex:none;}
  .firm{position:absolute;right:36px;top:12px;text-align:right;}
  .firm-name{margin:0;font-family:"Anton",sans-serif;font-weight:400;font-size:34px;line-height:40px;color:var(--white);}
  .firm-tag{margin:4px 0 0;font-family:"Lato",sans-serif;font-style:italic;font-weight:700;font-size:11px;color:var(--white);}
</style>
</head>
<body>
<div class="flyer">
  <header class="masthead"><h1>Nine Rung Ledger Remedy Seminar Agenda</h1></header>

  <section class="step" style="top:109px;height:117px;">
    <div class="step-text"><p>We will first show you how to eliminate much of your self-employment tax on your return by converting your business into an S Corporation. A business owner making over <b>$120,000</b> per year can save about <b>$12,000</b> per year by doing this.</p></div>
    <div class="step-badge"><span>Step</span><span>1</span></div>
    <div class="step-photo photo-selfemploy" role="img" aria-label="Sticky note reading self employment tax on top of cash"></div>
  </section>

  <section class="step" style="top:247px;height:121px;">
    <div class="step-text"><p>We will show you how to get tax free income from your corporation by renting you home to the corporation for the board meetings.Many of our clients are getting up to <b>$21,000</b> in tax free income which could put <b>$8,400</b> cash into your pocket.</p></div>
    <div class="step-badge"><span>Step</span><span>2</span></div>
    <div class="step-photo photo-keys" role="img" aria-label="House keys handed over above a lease agreement"></div>
  </section>

  <section class="step" style="top:410px;height:98px;">
    <div class="step-text"><p>We will show you the easiest way to track your expenses so that the only thing you will have to do to have rock solid books is to take a picture of the receipt and throw it away. It doesn't get any better than that.</p></div>
    <div class="step-badge"><span>Step</span><span>3</span></div>
    <div class="step-photo photo-notebook" role="img" aria-label="Spiral notebook titled tracking your expenses with pencils"></div>
  </section>

  <section class="step" style="top:550px;height:94px;">
    <div class="step-text"><p>Next, we show you the importance of tax planning and why it is critical to meet with your CPA before the end of the year and not just when you do your tax preparation.</p></div>
    <div class="step-badge"><span>Step</span><span>4</span></div>
    <div class="step-photo photo-planning" role="img" aria-label="Notepad reading tax planning beside a calculator"></div>
  </section>

  <section class="step" style="top:691px;height:89px;">
    <div class="step-text"><p>We will show you how to hire your children and get <b>$7,500</b> per child tax free. This will save you <b>$3,000</b> per child in income tax reduction.</p></div>
    <div class="step-badge"><span>Step</span><span>5</span></div>
    <div class="step-photo photo-taxcut" role="img" aria-label="Red block letters spelling tax being cut by scissors"></div>
  </section>

  <section class="step" style="top:827px;height:99px;">
    <div class="step-text"><p>We will discuss how to make your child's college education tax deductible. With college cost spiraling out of control this is a biggie. Most of our clients have a savings of about <b>$12,000</b> per year of college.</p></div>
    <div class="step-badge"><span>Step</span><span>6</span></div>
    <div class="step-photo photo-desk" role="img" aria-label="Desk with laptop showing charts, glasses and stationery"></div>
  </section>

  <section class="step" style="top:955px;height:114px;">
    <div class="step-text"><p>Our grand finale is to show you how to use, not one, but two corporations to get a several hundred thousand dollar tax deferral, get an interest free loan from the government and use that money to grow your business and your wealth.</p></div>
    <div class="step-badge"><span>Step</span><span>7</span></div>
    <div class="step-photo photo-card" role="img" aria-label="Hand holding a card reading 0% interest free" style="bottom:8px;"></div>
  </section>

  <footer class="footer">
    <p class="motto">If they drive by with a machine gun you don't have to stand up.</p>
    <div class="contact">
      <div class="contact-row">
        <span class="contact-item"><svg viewBox="0 0 24 24"><path d="M12 2a7 7 0 0 0-7 7c0 5 7 13 7 13s7-8 7-13a7 7 0 0 0-7-7zm0 9.5A2.5 2.5 0 1 1 12 6.5a2.5 2.5 0 0 1 0 5z"/></svg>2280 E. Orchard Ave, Ste. B, Dalton, CA 95410</span>
        <span class="contact-item"><svg viewBox="0 0 24 24"><path d="M6.6 10.8a15 15 0 0 0 6.6 6.6l2.2-2.2c.3-.3.7-.4 1-.2 1.1.4 2.3.6 3.6.6.6 0 1 .4 1 1V20c0 .6-.4 1-1 1A17 17 0 0 1 3 4c0-.6.4-1 1-1h3.5c.6 0 1 .4 1 1 0 1.3.2 2.5.6 3.6.1.3 0 .7-.2 1z"/></svg>555-014-2271</span>
        <span class="contact-item" style="margin-left:14px;"><svg viewBox="0 0 24 24"><path d="M6 2h9v6H6zM4 9h16v11H4zm3 3v2h3v-2zm5 0v2h3v-2zm-5 4v2h3v-2zm5 0v2h3v-2z"/></svg>555-014-2290</span>
      </div>
      <div class="contact-row">
        <span class="contact-item"><svg viewBox="0 0 24 24"><path d="M2 5h20v14H2zm2 2v.5l8 5 8-5V7l-8 5z"/></svg>Marlow@tallwaterfigures.com \ Dean@tallwaterfigures.com</span>
        <span class="contact-item"><svg viewBox="0 0 24 24"><path d="M12 2a10 10 0 1 0 0 20 10 10 0 0 0 0-20zm6.9 9h-3a15 15 0 0 0-1.3-6A8 8 0 0 1 18.9 11zM12 4c.9 1.3 1.7 3.9 1.9 7h-3.8c.2-3.1 1-5.7 1.9-7zM9.4 5a15 15 0 0 0-1.3 6h-3A8 8 0 0 1 9.4 5zm-4.3 8h3a15 15 0 0 0 1.3 6 8 8 0 0 1-4.3-6zM12 20c-.9-1.3-1.7-3.9-1.9-7h3.8c-.2 3.1-1 5.7-1.9 7zm2.6-1a15 15 0 0 0 1.3-6h3a8 8 0 0 1-4.3 6z"/></svg>www.tallwaterfigurescpa.com</span>
      </div>
    </div>
    <div class="firm">
      <p class="firm-name">Tallwater Figures</p>
      <p class="firm-tag">A Professional Accounting Corporation</p>
    </div>
  </footer>
</div>
</body>
</html>
```